Creative UI design for web application

I need a new UI design for my web application. It will be used by small and micro business owners to plan & implement growth tactics.

I've attached the current design (which I'm open to be changed) - but in particular I need to design the centre of the screen, where the work actually happens.

There needs to be place for a title (YOUR BUSINESS) and description (say 1-2 paragraphs of text) - and am happy to include icons or imagery where makes sense. It may make sense for the user to be able to upload their business logo and name, for example.

This screen will be used by the business owner to understand the real value they offer potential customers and their point of difference - why they exist and why potential customers should care.

They'll use the information they put into this screen to plan things like their messaging.

Following that, there needs to be 2 sections in the dashboard.

The first section is titled "WHO YOU ARE"

The first section will include a number of boxes that the user can input information into, as follows:

- Logo
- Business name
- Business tag line
- Business vision
- Business bio
- Brand colours (these should end up as swatches based on the colour code they enter) - the colour code for each colour swatch should also be visible.
- Key competitors
- SWOT analysis (boxes to enter their strengths, weaknesses, opportunities and threats).

The second section is titled "WHY YOU EXIST"

The second section will include a number of boxes that the user can input information (text) into, as follows:

- Who are your ideal customers?
- What problem are you trying to solve for them?
- What pain points will this remove for them?
- How do you solve it?
- How else could this problem be solved?
- Who offers these other solutions?
- Why is your solution better?
- How much does your solution cost?
- What value are you providing to justify this cost?
- How will this make their life/job easier/better?

They should be able to write a decent amount of information in the boxes.

There should ideally be a place for a description for each of these text fields (for both section 1 & 2) as well so I can give them a little bit more direction around what to put in the box. Alternatively there could be a little icon (say a question mark or "i") that they could click on to view instructions. The instructions will be around 2-4 sentences long for each text field.

You have 2 options:

a) This all needs to appear on the one screen, and the navigation needs to be visible (as per the example attached but feel free to recreate this navigation)

Note: the page can scroll below the fold - but please provide the design for the full length of the page.

b) Potentially the 2 sections could actually be in 2 different items in the menu - YOUR BUSINESS and YOUR VALUE (which would sit next to YOUR BUSINESS and before YOUR CUSTOMER in the screenshot provided). feel free to design them as 2 separate screens if you prefer.

I have attached a screenshot of the app as it stands today (screen shot 2017) which would still exist in the new design but under a different section (the learn section from the plan2 mockup attached)

I have mocked up how this new screen could look if broken into 2 and that's also attached. If you can make this come to life - and look more engaging that would be helpful! :)

Target Market(s)

Small and micro business owners

Industry/Entity Type

Marketing

Number of Pages Required

1 page

Font styles to use
Sans Serif
Other font styles liked:
• Montserrat

Colors
87cfc6
d2a4cc
ffffff
85cae6
e8e8e8
5c5c5c

Requirements
Must have
• Use of my brand colours: #cc8eb2, #76d6c8, #68c7ff as well as white and #595959. Must be visually pleasing / engaging, designed for desktop (as it's a desktop application), really easy to use / navigate.
• Use font Montserrat light & Montserrat Regular or Bold. Mostly should be Montserrat light.
Nice to have
• Would be nice to see how this would look on mobile (as the application is responsive) but this is not mandatory.
Should not have
• Should not look too corporate or dry.

```html
<!DOCTYPE html>
<html lang="en">
<head>
<meta charset="utf-8">
<title>Your Business – Who You Are</title>
<link href="https://fonts.googleapis.com/css2?family=Montserrat:wght@300;400;500;600;700&display=swap" rel="stylesheet">
<style>
  :root {
    --bar: #595959;
    --pink: #cc8eb2;
    --teal: #76d6c8;
    --blue: #6cc6fb;
    --panel: #f2f2f4;
    --field: #f8f8fa;
    --field-border: #d6d6da;
    --label: #4f4f4f;
    --hint: #b4b4b8;
    --tip: #555555;
    --white: #ffffff;
  }
  * { box-sizing: border-box; margin: 0; padding: 0; }
  html, body { width: 1200px; height: 1200px; overflow: hidden; background: var(--white); }
  body { position: relative; font-family: 'Montserrat', sans-serif; color: var(--label); }

  .topbar { position: absolute; left: 0; top: 0; width: 1200px; height: 38px; background: var(--bar); }
  .brand { position: absolute; left: 124px; top: 11px; font-size: 15px; font-weight: 400; letter-spacing: 0.5px; color: var(--white); }
  .nav-link { position: absolute; top: 12px; font-size: 13px; font-weight: 500; color: var(--white); }
  .nav-link.is-active { top: 7px; left: 319px; width: 66px; height: 24px; border: 1px solid var(--teal); border-radius: 12px; color: var(--teal); text-align: center; line-height: 22px; }
  .profile { position: absolute; right: 186px; top: 11px; font-size: 14px; font-weight: 500; color: var(--white); }
  .profile svg { margin-left: 6px; vertical-align: middle; }

  .tabs { position: absolute; left: 118px; top: 62px; height: 42px; display: flex; }
  .tab { height: 42px; line-height: 42px; background: var(--blue); color: var(--white); font-size: 13px; font-weight: 500; text-align: center; border-right: 1px solid #5ab9f0; }
  .tab:last-child { border-right: none; border-radius: 0 2px 2px 0; }
  .tab.is-current { background: var(--pink); border-right: none; border-radius: 2px 0 0 2px; position: relative; }
  .tab.is-current::after { content: ""; position: absolute; left: 57px; bottom: -6px; border-left: 6px solid transparent; border-right: 6px solid transparent; border-top: 6px solid var(--pink); }

  .panel { position: absolute; left: 118px; top: 132px; width: 982px; height: 1030px; background: var(--panel); }
  .section-title { position: absolute; left: 153px; top: 161px; font-size: 17px; font-weight: 700; color: var(--pink); letter-spacing: 0.3px; }
  .section-rule { position: absolute; left: 153px; top: 188px; width: 875px; height: 1px; background: #9c9c9c; }

  .label { position: absolute; font-size: 12.5px; font-weight: 500; color: var(--label); display: flex; align-items: center; height: 20px; }
  .help { display: inline-block; width: 19px; height: 19px; margin-left: 6px; border-radius: 50%; background: var(--teal); color: var(--white); font-size: 10px; text-align: center; line-height: 19px; font-weight: 500; }

  .field { position: absolute; background: var(--field); border: 1px solid var(--field-border); border-radius: 3px; }
  .field .placeholder { position: absolute; top: 12px; font-size: 11px; font-weight: 300; color: var(--hint); }
  .grip { position: absolute; right: 3px; bottom: 3px; }

  .tooltip { position: absolute; left: 242px; top: 262px; width: 314px; height: 28px; background: var(--tip); border-radius: 3px; color: var(--white); font-size: 11.5px; font-weight: 300; text-align: center; line-height: 28px; }
  .tooltip::after { content: ""; position: absolute; left: 36px; bottom: -5px; border-left: 5px solid transparent; border-right: 5px solid transparent; border-top: 5px solid var(--tip); }

  .save { position: absolute; left: 896px; top: 1086px; width: 134px; height: 39px; border-radius: 20px; background: var(--teal); color: var(--white); font-size: 14px; font-weight: 700; text-align: center; line-height: 39px; }
</style>
</head>
<body>
  <header class="topbar">
    <div class="brand">GAINLEAF</div>
    <div class="nav-link is-active">Plan</div>
    <div class="nav-link" style="left:403px">Learn</div>
    <div class="nav-link" style="left:472px">Remember</div>
    <div class="profile">My Profile<svg width="8" height="5" viewBox="0 0 8 5"><path d="M0 0h8L4 5z" fill="#fff"/></svg></div>
  </header>

  <nav class="tabs">
    <div class="tab is-current" style="width:137px">Your Business</div>
    <div class="tab" style="width:109px">Your Value</div>
    <div class="tab" style="width:130px">Your Product</div>
    <div class="tab" style="width:148px">Your Customers</div>
    <div class="tab" style="width:114px">Your Goals</div>
    <div class="tab" style="width:132px">Your Plan</div>
  </nav>

  <main class="panel"></main>
  <h1 class="section-title">WHO YOU ARE</h1>
  <div class="section-rule"></div>

  <div class="label" style="left:155px;top:210px">Upload your company Logo</div>
  <div class="field" style="left:154px;top:238px;width:416px;height:37px">
    <svg style="position:absolute;left:12px;top:12px" width="18" height="12" viewBox="0 0 18 12"><path d="M4 12a4 4 0 0 1-.5-8A5.5 5.5 0 0 1 14 3.5 4.3 4.3 0 0 1 14 12z" fill="#b9b9bd"/><path d="M9 4l3 3h-2v3H8V7H6z" fill="#f8f8fa"/></svg>
    <span class="placeholder" style="left:39px">Upload Logo File, JPG or PNG</span>
  </div>

  <div class="label" style="left:616px;top:210px">Business name</div>
  <div class="field" style="left:614px;top:238px;width:416px;height:37px">
    <span class="placeholder" style="left:13px">Type Your Business Name</span>
  </div>

  <div class="label" style="left:155px;top:296px">Business Tag Line<span class="help">?</span></div>
  <div class="field" style="left:154px;top:322px;width:416px;height:38px"></div>

  <div class="label" style="left:616px;top:296px">Brand colours</div>
  <div class="field" style="left:614px;top:322px;width:416px;height:38px"></div>

  <div class="tooltip">Explain the value of your business in 5 words or less</div>

  <div class="label" style="left:155px;top:380px">Business Bio<span class="help">?</span></div>
  <div class="field" style="left:154px;top:408px;width:416px;height:122px"><svg class="grip" width="7" height="7" viewBox="0 0 7 7" fill="#bbb"><circle cx="6" cy="1" r=".7"/><circle cx="3.5" cy="3.5" r=".7"/><circle cx="6" cy="3.5" r=".7"/><circle cx="1" cy="6" r=".7"/><circle cx="3.5" cy="6" r=".7"/><circle cx="6" cy="6" r=".7"/></svg></div>

  <div class="label" style="left:616px;top:380px">Business Vision<span class="help">?</span></div>
  <div class="field" style="left:614px;top:408px;width:416px;height:122px"><svg class="grip" width="7" height="7" viewBox="0 0 7 7" fill="#bbb"><circle cx="6" cy="1" r=".7"/><circle cx="3.5" cy="3.5" r=".7"/><circle cx="6" cy="3.5" r=".7"/><circle cx="1" cy="6" r=".7"/><circle cx="3.5" cy="6" r=".7"/><circle cx="6" cy="6" r=".7"/></svg></div>

  <div class="label" style="left:155px;top:550px">Key Competitors<span class="help">?</span></div>
  <div class="field" style="left:154px;top:578px;width:876px;height:122px"><svg class="grip" width="7" height="7" viewBox="0 0 7 7" fill="#bbb"><circle cx="6" cy="1" r=".7"/><circle cx="3.5" cy="3.5" r=".7"/><circle cx="6" cy="3.5" r=".7"/><circle cx="1" cy="6" r=".7"/><circle cx="3.5" cy="6" r=".7"/><circle cx="6" cy="6" r=".7"/></svg></div>

  <div class="label" style="left:155px;top:720px">Strengths<span class="help">?</span></div>
  <div class="field" style="left:154px;top:748px;width:416px;height:122px"><svg class="grip" width="7" height="7" viewBox="0 0 7 7" fill="#bbb"><circle cx="6" cy="1" r=".7"/><circle cx="3.5" cy="3.5" r=".7"/><circle cx="6" cy="3.5" r=".7"/><circle cx="1" cy="6" r=".7"/><circle cx="3.5" cy="6" r=".7"/><circle cx="6" cy="6" r=".7"/></svg></div>

  <div class="label" style="left:616px;top:720px">Weaknesses<span class="help">?</span></div>
  <div class="field" style="left:614px;top:748px;width:416px;height:122px"><svg class="grip" width="7" height="7" viewBox="0 0 7 7" fill="#bbb"><circle cx="6" cy="1" r=".7"/><circle cx="3.5" cy="3.5" r=".7"/><circle cx="6" cy="3.5" r=".7"/><circle cx="1" cy="6" r=".7"/><circle cx="3.5" cy="6" r=".7"/><circle cx="6" cy="6" r=".7"/></svg></div>

  <div class="label" style="left:155px;top:890px">Opportunities<span class="help">?</span></div>
  <div class="field" style="left:154px;top:918px;width:416px;height:122px"><svg class="grip" width="7" height="7" viewBox="0 0 7 7" fill="#bbb"><circle cx="6" cy="1" r=".7"/><circle cx="3.5" cy="3.5" r=".7"/><circle cx="6" cy="3.5" r=".7"/><circle cx="1" cy="6" r=".7"/><circle cx="3.5" cy="6" r=".7"/><circle cx="6" cy="6" r=".7"/></svg></div>

  <div class="label" style="left:616px;top:890px">Threats<span class="help">?</span></div>
  <div class="field" style="left:614px;top:918px;width:416px;height:122px"><svg class="grip" width="7" height="7" viewBox="0 0 7 7" fill="#bbb"><circle cx="6" cy="1" r=".7"/><circle cx="3.5" cy="3.5" r=".7"/><circle cx="6" cy="3.5" r=".7"/><circle cx="1" cy="6" r=".7"/><circle cx="3.5" cy="6" r=".7"/><circle cx="6" cy="6" r=".7"/></svg></div>

  <div class="save">Save Changes</div>
</body>
</html>
```